Webdesign

We are value investment firm in Denver, Colorado. We are a small but a very unique firm. We are looking for a minimalistic and clean design. We are competing against competitors that usually larger than we are, but we need to have a design that is better than theirs. Our clients put a tremendous trust in us when they let us manage their life savings. This website has to communicate trust but without traditional cliches (dollar bills, glasses, Harbor Ledger Gazette).
We had a coder/designer create our current website a few weeks ago http://brightkestrel.example/tolvan , we are not thrilled about the design. We are attaching our company's presentation, we'd like the design to be closer to the colors of that presentation.
We are looking for both design and coding (wordpress).
Updates
we will pay additional $200 for wordpress implementation
A few points of clarifications about design:
- don't use pictures of strangers
- we are a Denver/Colorado firm, if you use pictures use Denver/Colorado pictures
- full width website is probably what we are looking
- maybe parallax type of design
This theme http://quillframe.example/WP/Nimbra/ is how we see the new design
Industry/Entity Type
Investment

```html
<!DOCTYPE html>
<html lang="en">
<head>
<meta charset="utf-8">
<title>Tolvan Capital — Value Investment Firm</title>
<link rel="stylesheet" href="https://fonts.googleapis.com/css2?family=Raleway:wght@300;400;600;700&family=Open+Sans:wght@400;600;700&display=swap">
<style>
:root{
  --navy:#14213d;
  --navy-deep:#0f1a33;
  --blue:#1d5aa8;
  --blue-soft:#3a78c4;
  --teal:#2fd3a5;
  --charcoal:#22262d;
  --ink:#3a3f47;
  --muted:#8a9099;
  --line:#e3e6ea;
  --white:#ffffff;
}
*{box-sizing:border-box;margin:0;padding:0}
html,body{width:1200px;height:4932px;overflow:hidden}
body{font-family:"Open Sans",Arial,sans-serif;color:var(--ink);background:var(--white);position:relative}
.section{position:absolute;left:0;width:1200px;overflow:hidden}
.heading{font-family:"Raleway",Arial,sans-serif;font-weight:300;text-transform:uppercase;text-align:center;color:var(--blue);font-size:46px;line-height:56px;letter-spacing:1px}
.ornament{display:block;margin:14px auto 0}
.subheading{font-family:"Raleway",Arial,sans-serif;font-weight:700;font-size:14px;text-transform:uppercase;text-align:center;color:var(--navy);letter-spacing:1px}
.body-copy{font-size:14px;line-height:24px;color:var(--muted);text-align:center}

/* Hero */
.hero{top:0;height:800px;background:linear-gradient(180deg,#2a4a7e 0%,#1f3b6a 45%,#16294f 100%)}
.hero-photo{position:absolute;inset:0;background:linear-gradient(160deg,rgba(120,150,200,.45) 0%,rgba(40,70,120,.2) 40%,rgba(10,20,45,.5) 100%)}
.nav{position:absolute;top:0;left:0;width:1200px;height:80px;background:rgba(12,22,46,.55)}
.brand{position:absolute;left:20px;top:6px;height:68px;width:150px;background:var(--white);display:flex;align-items:center;justify-content:center;gap:8px}
.brand-mark{width:14px;height:14px;background:var(--navy)}
.brand-name{font-family:"Raleway",Arial,sans-serif;font-weight:700;font-size:19px;color:var(--navy)}
.nav-links{position:absolute;right:40px;top:24px;display:flex;gap:6px;list-style:none}
.nav-links li{font-family:"Raleway",Arial,sans-serif;font-weight:600;font-size:14px;color:var(--white);text-transform:uppercase;padding:7px 14px;letter-spacing:.5px}
.nav-links .active{background:var(--blue)}
.nav-search{width:34px;height:32px;background:rgba(255,255,255,.15);display:flex;align-items:center;justify-content:center;padding:0!important}
.hero-title{position:absolute;right:110px;top:215px;width:860px;text-align:right;font-family:"Raleway",Arial,sans-serif;font-weight:700;font-size:32px;line-height:40px;color:var(--white);text-transform:uppercase}
.hero-text{position:absolute;left:250px;top:370px;width:840px;font-size:15px;line-height:25px;color:#d5def0;text-align:center}
.hero-cut{position:absolute;left:0;bottom:0}

/* About */
.about{top:800px;height:370px}
.about .heading{margin-top:50px}
.about .subheading{margin-top:18px}
.about .body-copy{width:900px;margin:20px auto 0}
.btn-outline{display:block;width:150px;height:38px;margin:18px auto 0;border:1px solid var(--blue-soft);color:var(--blue);font-family:"Raleway",Arial,sans-serif;font-weight:600;font-size:13px;text-transform:uppercase;text-align:center;line-height:36px;letter-spacing:1px}

/* Quote band */
.band{top:1170px;height:475px}
.band-photo{position:absolute;inset:0;background:linear-gradient(120deg,#1b3568 0%,#2a4d8a 45%,#13264e 100%)}
.band-text{position:absolute;left:585px;top:190px;width:440px;font-family:"Raleway",Arial,sans-serif;font-weight:300;font-size:24px;line-height:34px;color:var(--white);text-transform:uppercase}

/* Services */
.services{top:1645px;height:600px}
.services .heading{margin-top:70px}
.services .subheading{margin-top:20px}
.service-grid{position:absolute;left:100px;top:265px;width:1000px;display:flex;gap:24px}
.service-card{width:232px;height:200px;background:var(--white);border:1px solid var(--line);box-shadow:0 3px 10px rgba(0,0,0,.08);text-align:center;padding-top:68px;position:relative}
.service-card.featured{background:var(--navy)}
.service-icon{position:absolute;left:91px;top:-22px;width:50px;height:50px;transform:rotate(45deg);background:var(--navy);border:3px solid var(--white);box-shadow:0 0 0 1px var(--line)}
.service-card.featured .service-icon{background:var(--blue)}
.service-icon svg{transform:rotate(-45deg);position:absolute;left:11px;top:11px}
.service-title{font-family:"Raleway",Arial,sans-serif;font-weight:700;font-size:14px;text-transform:uppercase;color:var(--navy);line-height:19px}
.service-card.featured .service-title{color:var(--white)}
.service-text{font-size:12px;line-height:18px;color:var(--muted);margin:10px 20px 0}
.service-card.featured .service-text{color:#b9c4da}

/* Process */
.process{top:2200px;height:512px;background:transparent}
.process-bg{position:absolute;left:0;top:0}
.process .heading{color:var(--white);font-size:34px;position:absolute;top:160px;width:1200px}
.donut{position:absolute;top:280px;width:170px;height:220px;text-align:center}
.donut svg{display:block}
.donut-value{position:absolute;left:0;top:66px;width:170px;text-align:center;font-family:"Raleway",Arial,sans-serif;font-weight:600;font-size:28px;line-height:38px;color:var(--white)}
.donut-label{margin-top:14px;font-family:"Raleway",Arial,sans-serif;font-weight:700;font-size:14px;color:var(--white);text-transform:uppercase;letter-spacing:1px}

/* Team */
.team{top:2712px;height:638px}
.team .heading{margin-top:115px}
.team .subheading{margin-top:42px}
.team-grid{position:absolute;left:255px;top:308px;display:flex;gap:10px}
.team-photo{width:165px;height:290px;background:linear-gradient(180deg,#c9ccd0 0%,#a9adb3 60%,#7d828a 100%);position:relative}
.team-photo.alt{background:linear-gradient(180deg,#d8d3cc 0%,#b5aea4 60%,#857d73 100%)}
.team-caption{position:absolute;left:0;bottom:0;width:165px;height:40px;background:var(--teal);color:var(--white);font-family:"Raleway",Arial,sans-serif;font-weight:700;font-size:13px;text-transform:uppercase;text-align:center;line-height:40px}
.team-social{position:absolute;left:32px;top:170px;display:flex;gap:10px}
.team-social span{width:40px;height:40px;border-radius:50%;background:rgba(47,211,165,.9);display:block}

/* Testimonial */
.testimonial{top:3350px;height:390px;background:var(--navy)}
.quote-mark{position:absolute;top:62px;width:1200px;text-align:center;font-family:"Raleway",Arial,sans-serif;font-weight:700;font-size:60px;color:var(--teal);line-height:60px}
.quote-text{position:absolute;left:185px;top:140px;width:830px;font-size:14px;line-height:23px;color:#c5cee0;text-align:center;font-style:italic}
.quote-name{position:absolute;top:228px;width:1200px;text-align:center;font-family:"Raleway",Arial,sans-serif;font-weight:600;font-size:14px;color:var(--white)}
.quote-people{position:absolute;left:537px;top:268px;display:flex;gap:12px}
.quote-people span{width:36px;height:36px;border-radius:50%;background:linear-gradient(180deg,#8c94a4,#5a6376);border:2px solid var(--white);display:block}
.quote-people span.current{border-color:var(--teal)}

/* News */
.news{top:3740px;height:658px}
.news .heading{margin-top:165px}
.news .subheading{margin-top:24px}
.news-grid{position:absolute;left:100px;top:330px;display:flex;gap:25px}
.news-card{width:316px;height:290px;background:var(--white);box-shadow:0 3px 10px rgba(0,0,0,.08);position:relative}
.news-image{height:150px;background:linear-gradient(135deg,#e4ecf4 0%,#b9c9dc 60%,#8aa1bd 100%)}
.news-date{position:absolute;left:12px;top:12px;width:52px;height:56px;background:var(--teal);color:var(--white);text-align:center;font-family:"Raleway",Arial,sans-serif;font-weight:700}
.news-date b{display:block;font-size:22px;line-height:30px;margin-top:4px}
.news-date i{display:block;font-style:normal;font-size:11px;text-transform:uppercase}
.news-title{font-family:"Raleway",Arial,sans-serif;font-weight:700;font-size:15px;color:var(--navy);text-transform:uppercase;margin:18px 18px 0}
.news-text{font-size:12px;line-height:18px;color:var(--muted);margin:8px 18px 0}

/* Contact */
.contact{top:4398px;height:492px;background:var(--navy-deep)}
.contact-title{position:absolute;left:100px;top:90px;font-family:"Raleway",Arial,sans-serif;font-weight:300;font-size:34px;color:var(--white);text-transform:uppercase}
.contact-list{position:absolute;left:100px;top:160px;list-style:none;width:400px}
.contact-list li{display:flex;gap:14px;align-items:flex-start;font-size:13px;line-height:20px;color:#a8b3c8;margin-bottom:16px}
.contact-list svg{flex:none;margin-top:2px}
.contact-form{position:absolute;left:575px;top:90px;width:525px;display:grid;grid-template-columns:1fr 1fr;gap:14px}
.field{height:40px;border:1px solid #2f3d5c;background:rgba(255,255,255,.03);font-size:12px;color:#8d98ae;padding:11px 12px}
.field.message{grid-column:1 / 3;height:150px}
.btn-send{grid-column:1 / 3;height:44px;background:var(--teal);color:var(--white);border:none;font-family:"Raleway",Arial,sans-serif;font-weight:700;font-size:14px;text-transform:uppercase;letter-spacing:1px;text-align:center;line-height:44px}

/* Footer */
.footer{top:4890px;height:42px;background:var(--white);text-align:center;font-size:12px;color:var(--muted);line-height:42px}
</style>
</head>
<body>

<header class="section hero">
  <div class="hero-photo" role="img" aria-label="Aerial view of the Denver city skyline in deep blue tones"></div>
  <nav class="nav">
    <div class="brand"><span class="brand-mark"></span><span class="brand-name">TOLVAN</span></div>
    <ul class="nav-links">
      <li class="active">Tolvan</li>
      <li>About Us</li>
      <li>Invest Differently</li>
      <li>Content</li>
      <li>Career</li>
      <li>Contact Us</li>
      <li class="nav-search"><svg width="14" height="14" viewBox="0 0 14 14"><circle cx="6" cy="6" r="4.5" fill="none" stroke="#fff" stroke-width="1.6"/><line x1="9.3" y1="9.3" x2="13" y2="13" stroke="#fff" stroke-width="1.8"/></svg></li>
    </ul>
  </nav>
  <h1 class="hero-title">Our Goal<br>to preserve and grow our clients’<br>wealth while letting them sleep well at night.</h1>
  <p class="hero-text">A disciplined, process-driven, value investment firm that provides a private portfolio management service tailored to individual and institutional clients who seek steady, careful growth over the long run.</p>
  <svg class="hero-cut" width="1200" height="80" viewBox="0 0 1200 80"><polygon points="0,80 1200,10 1200,80" fill="#fff"/></svg>
</header>

<section class="section about">
  <h2 class="heading">More About Us</h2>
  <svg class="ornament" width="120" height="12" viewBox="0 0 120 12"><line x1="0" y1="6" x2="50" y2="6" stroke="#c9d3e2"/><rect x="55" y="1" width="8" height="8" transform="rotate(45 59 5)" fill="#1d5aa8"/><line x1="70" y1="6" x2="120" y2="6" stroke="#c9d3e2"/></svg>
  <p class="subheading">Tolvan Capital — Who We Are</p>
  <p class="body-copy">A disciplined, process-driven, value investment firm that provides a private portfolio management service tailored to individual and institutional clients. Most of our clients come to us through referrals from people who already trust us with their savings.<br>We are a fee-only registered investment adviser, we are registered with our home state of Colorado and act in the best interest of every client we serve.</p>
  <span class="btn-outline">Read More</span>
</section>

<section class="section band">
  <div class="band-photo" role="img" aria-label="Suspension bridge at dusk in deep blue tones"></div>
  <p class="band-text">The investment process should incorporate both analytical and behavioral aspects</p>
</section>

<section class="section services">
  <h2 class="heading">Our Services</h2>
  <svg class="ornament" width="120" height="12" viewBox="0 0 120 12"><line x1="0" y1="6" x2="50" y2="6" stroke="#c9d3e2"/><rect x="55" y="1" width="8" height="8" transform="rotate(45 59 5)" fill="#1d5aa8"/><line x1="70" y1="6" x2="120" y2="6" stroke="#c9d3e2"/></svg>
  <p class="subheading">Invest Differently</p>
  <div class="service-grid">
    <div class="service-card">
      <span class="service-icon"><svg width="22" height="22" viewBox="0 0 22 22"><circle cx="11" cy="7" r="4" fill="none" stroke="#fff" stroke-width="2"/><path d="M3 20c1-5 15-5 16 0" fill="none" stroke="#fff" stroke-width="2"/></svg></span>
      <h3 class="service-title">We Are<br>Different</h3>
      <p class="service-text">Our value-based approach is shaped carefully for lasting results…</p>
    </div>
    <div class="service-card featured">
      <span class="service-icon"><svg width="22" height="22" viewBox="0 0 22 22"><polyline points="2,17 8,10 12,14 20,4" fill="none" stroke="#fff" stroke-width="2"/></svg></span>
      <h3 class="service-title">Investment<br>Process</h3>
      <p class="service-text">We look for lasting value, hidden in the market and the industry…</p>
    </div>
    <div class="service-card">
      <span class="service-icon"><svg width="22" height="22" viewBox="0 0 22 22"><circle cx="11" cy="11" r="8" fill="none" stroke="#fff" stroke-width="2"/><polyline points="11,6 11,11 15,13" fill="none" stroke="#fff" stroke-width="2"/></svg></span>
      <h3 class="service-title">Socrates<br>Market</h3>
      <p class="service-text">Many businesses, but we do the work to see the facts on record…</p>
    </div>
    <div class="service-card">
      <span class="service-icon"><svg width="22" height="22" viewBox="0 0 22 22"><rect x="3" y="11" width="4" height="8" fill="#fff"/><rect x="9" y="6" width="4" height="13" fill="#fff"/><rect x="15" y="2" width="4" height="17" fill="#fff"/></svg></span>
      <h3 class="service-title">Why We<br>Build Models</h3>
      <p class="service-text">Our investment process is both quantitative and qualitative…</p>
    </div>
  </div>
</section>

<section class="section process">
  <svg class="process-bg" width="1200" height="512" viewBox="0 0 1200 512" role="img" aria-label="Dark textured background"><polygon points="0,70 600,0 1200,70 1200,512 0,512" fill="#22262d"/></svg>
  <h2 class="heading">Investment Process</h2>
  <svg class="ornament" style="position:absolute;left:540px;top:215px;margin:0" width="120" height="12" viewBox="0 0 120 12"><line x1="0" y1="6" x2="50" y2="6" stroke="#555b66"/><rect x="55" y="1" width="8" height="8" transform="rotate(45 59 5)" fill="#2fd3a5"/><line x1="70" y1="6" x2="120" y2="6" stroke="#555b66"/></svg>

  <div class="donut" style="left:115px">
    <svg width="170" height="170" viewBox="0 0 170 170"><circle cx="85" cy="85" r="70" fill="none" stroke="#fff" stroke-width="16"/><circle cx="85" cy="85" r="70" fill="none" stroke="#2fd3a5" stroke-width="16" stroke-dasharray="246.3 439.8" transform="rotate(-90 85 85)"/></svg>
    <span class="donut-value">56.0%</span>
    <p class="donut-label">Discovery</p>
  </div>
  <div class="donut" style="left:382px">
    <svg width="170" height="170" viewBox="0 0 170 170"><circle cx="85" cy="85" r="70" fill="none" stroke="#fff" stroke-width="16"/><circle cx="85" cy="85" r="70" fill="none" stroke="#2fd3a5" stroke-width="16" stroke-dasharray="351.9 439.8" transform="rotate(-90 85 85)"/></svg>
    <span class="donut-value">80.0%</span>
    <p class="donut-label">Research</p>
  </div>
  <div class="donut" style="left:648px">
    <svg width="170" height="170" viewBox="0 0 170 170"><circle cx="85" cy="85" r="70" fill="none" stroke="#fff" stroke-width="16"/><circle cx="85" cy="85" r="70" fill="none" stroke="#2fd3a5" stroke-width="16" stroke-dasharray="131.9 439.8" transform="rotate(-90 85 85)"/></svg>
    <span class="donut-value">30.0%</span>
    <p class="donut-label">Maintenance</p>
  </div>
  <div class="donut" style="left:915px">
    <svg width="170" height="170" viewBox="0 0 170 170"><circle cx="85" cy="85" r="70" fill="none" stroke="#fff" stroke-width="16"/><circle cx="85" cy="85" r="70" fill="none" stroke="#2fd3a5" stroke-width="16" stroke-dasharray="395.8 439.8" transform="rotate(-90 85 85)"/></svg>
    <span class="donut-value">90.0%</span>
    <p class="donut-label">Selling</p>
  </div>
</section>

<section class="section team">
  <h2 class="heading">Meet Our Team</h2>
  <svg class="ornament" width="120" height="12" viewBox="0 0 120 12"><line x1="0" y1="6" x2="50" y2="6" stroke="#c9d3e2"/><rect x="55" y="1" width="8" height="8" transform="rotate(45 59 5)" fill="#1d5aa8"/><line x1="70" y1="6" x2="120" y2="6" stroke="#c9d3e2"/></svg>
  <p class="subheading">Meet Up Our Tolvan Team</p>
  <div class="team-grid">
    <div class="team-photo" role="img" aria-label="Portrait of a team member"></div>
    <div class="team-photo alt" role="img" aria-label="Portrait of Owen Hale">
      <div class="team-social"><span></span><span></span></div>
      <div class="team-caption">Owen Hale</div>
    </div>
    <div class="team-photo" role="img" aria-label="Portrait of a team member"></div>
    <div class="team-photo alt" role="img" aria-label="Portrait of a team member"></div>
  </div>
</section>

<section class="section testimonial">
  <div class="quote-mark">“</div>
  <p class="quote-text">“Tolvan has looked after our family savings for many years. They explain every decision plainly, they never chase fashions, and they answer the phone when markets turn rough. We sleep better knowing our money is handled with this much care and honesty.”</p>
  <p class="quote-name">Reid Calder</p>
  <div class="quote-people" role="img" aria-label="Client portraits"><span></span><span class="current"></span><span></span></div>
</section>

<section class="section news">
  <h2 class="heading">Our Latest News</h2>
  <svg class="ornament" width="120" height="12" viewBox="0 0 120 12"><line x1="0" y1="6" x2="50" y2="6" stroke="#c9d3e2"/><rect x="55" y="1" width="8" height="8" transform="rotate(45 59 5)" fill="#1d5aa8"/><line x1="70" y1="6" x2="120" y2="6" stroke="#c9d3e2"/></svg>
  <p class="subheading">Following Our Latest News</p>
  <div class="news-grid">
    <article class="news-card">
      <div class="news-image" role="img" aria-label="Businesswoman at a desk"></div>
      <div class="news-date"><b>25</b><i>Sep</i></div>
      <h3 class="news-title">Lorem Ipsum Simply Dummy</h3>
      <p class="news-text">Lorem ipsum is simply dummy text of the printing and typesetting industry, used here as placeholder.</p>
    </article>
    <article class="news-card">
      <div class="news-image" role="img" aria-label="Colleagues meeting in an office"></div>
      <div class="news-date"><b>25</b><i>Sep</i></div>
      <h3 class="news-title">Lorem Ipsum Simply Dummy</h3>
      <p class="news-text">Lorem ipsum is simply dummy text of the printing and typesetting industry, used here as placeholder.</p>
    </article>
    <article class="news-card">
      <div class="news-image" role="img" aria-label="Business team in discussion"></div>
      <div class="news-date"><b>25</b><i>Sep</i></div>
      <h3 class="news-title">Lorem Ipsum Simply Dummy</h3>
      <p class="news-text">Lorem ipsum is simply dummy text of the printing and typesetting industry, used here as placeholder.</p>
    </article>
  </div>
</section>

<section class="section contact">
  <h2 class="contact-title">Contact Info</h2>
  <ul class="contact-list">
    <li><svg width="14" height="18" viewBox="0 0 14 18"><path d="M7 1a6 6 0 0 1 6 6c0 4-6 10-6 10S1 11 1 7a6 6 0 0 1 6-6z" fill="none" stroke="#2fd3a5" stroke-width="1.6"/><circle cx="7" cy="7" r="2" fill="#2fd3a5"/></svg><span>1420 Larkspur Ave, Suite 300<br>Denver, CO 80202</span></li>
    <li><svg width="16" height="16" viewBox="0 0 16 16"><path d="M3 1h3l1.5 4-2 1.5a9 9 0 0 0 4 4L11 8.5l4 1.5v3a2 2 0 0 1-2 2A13 13 0 0 1 1 3a2 2 0 0 1 2-2z" fill="none" stroke="#2fd3a5" stroke-width="1.5"/></svg><span>Phone: (555) 014-2280<br>Fax: (555) 014-2281</span></li>
    <li><svg width="16" height="14" viewBox="0 0 16 14"><rect x="1" y="1" width="14" height="12" fill="none" stroke="#2fd3a5" stroke-width="1.5"/><polyline points="1,2 8,8 15,2" fill="none" stroke="#2fd3a5" stroke-width="1.5"/></svg><span>Email: contact@tolvancapital.example</span></li>
  </ul>
  <div class="contact-form">
    <div class="field">First Name</div>
    <div class="field">Last Name</div>
    <div class="field">Email</div>
    <div class="field">Your Phone</div>
    <div class="field message">Message</div>
    <div class="btn-send">Send Now</div>
  </div>
</section>

<footer class="section footer">© Copyright 2015 - Tolvan Capital. All rights reserved.</footer>

</body>
</html>
```